WERBE-FLYER
Zielgruppe
Immobilien Makler
Aufgabenstellung
Überarbeitung des bestehenden Entwurfs.
Der Flyer wird an Hauseigentümer mit der Post verteilt (nicht adressierte Werbung).
Format:
offen A4 Querformat
geschlossen (1x gefaltet) A5 (4 Seiten)
In der Mitte eine Perforationslinie zum Abtrennen. Danach kann die Seite 3 & 4 zusammengefaltet (geklebt) werden und an uns zurückgeschickt werden.
Rücksendung erfolgt via Geschäftsantwortsendung - ohne Strichcode (siehe Vorlage Alpin. Kurier).

```html
<!DOCTYPE html>
<html lang="de">
<head>
<meta charset="utf-8">
<title>Veluna Immobilien AG – Flyer</title>
<link href="https://fonts.googleapis.com/css2?family=Ubuntu:wght@400;500;700&family=Source+Sans+3:wght@400;600;700&display=swap" rel="stylesheet">
<style>
:root{
  --navy:#1f3550;
  --cyan:#1fb3cc;
  --stage:#979a9d;
  --paper:#ffffff;
  --strip:#e9eaeb;
  --ink:#2a2d31;
  --photo-sky:#c9d3dc;
  --photo-wall:#e8e6e1;
  --photo-ground:#8a8e8f;
}
*{margin:0;padding:0;box-sizing:border-box}
html,body{width:849px;height:1200px;overflow:hidden;background:var(--stage)}
body{position:relative;font-family:"Source Sans 3",sans-serif;color:var(--ink)}
.sheet{position:absolute;left:68px;width:715px;height:505px;background:var(--paper);overflow:hidden}
.sheet--cover{top:72px}
.sheet--inside{top:624px}
.abs{position:absolute}

/* cover */
.reply-mark{left:231px;top:3px;width:125px;height:62px}
.reply-mark .letter{position:absolute;left:21px;top:6px;font:700 25px "Source Sans 3",sans-serif;color:var(--ink)}
.reply-mark .note{position:absolute;left:67px;top:12px;font-size:3.6px;line-height:4.6px;color:#555}
.reply-mark .kind{position:absolute;left:12px;top:42px;width:112px;text-align:center;font-weight:700;font-size:3.8px;line-height:5px;color:var(--ink)}
.brand{display:flex;align-items:center;gap:6px;font-family:"Ubuntu",sans-serif;font-weight:500;color:var(--navy)}
.brand__square{width:8px;height:8px;background:var(--cyan)}
.brand--cover{left:528px;top:38px;font-size:24px;letter-spacing:1px}
.recipient{left:186px;top:102px;font-size:8px;line-height:11px}
.hero-photo{left:357px;top:102px;width:342px;height:271px;
  background:linear-gradient(180deg,var(--photo-sky) 0%,var(--photo-wall) 40%,#d8d4cc 65%,var(--photo-ground) 100%)}
.hero-edge{left:699px;top:102px;width:16px;height:307px;background:var(--navy)}
.hero-band{left:357px;top:373px;width:358px;height:36px;background:var(--navy);
  color:#fff;font:500 18.5px "Ubuntu",sans-serif;padding-left:34px;line-height:36px;letter-spacing:.2px}
.hero-accent{left:357px;top:409px;width:358px;height:5px;background:var(--cyan)}
.cover-url{right:37px;top:455px;font:700 11px "Ubuntu",sans-serif;color:var(--navy);letter-spacing:1px}

/* inside */
.side-bar{top:24px;width:15px;height:456px;background:var(--navy);border-bottom:4px solid var(--cyan)}
.side-bar--left{left:0}
.side-bar--right{right:0}
.perforation{left:357px;top:0;width:0;height:505px;border-left:1px dashed #9aa0a6}
.tape{left:358px;width:357px;height:24px;background:var(--strip);text-align:center;
  font:400 7.5px "Ubuntu",sans-serif;letter-spacing:1.3px;line-height:24px;color:var(--ink)}
.tape--top{top:0}
.tape--bottom{top:481px}
.scissors{left:350px;top:452px;width:14px;height:18px}
.page-title{font:700 19.5px "Ubuntu",sans-serif;color:var(--navy);line-height:24px}
.sub-title{font:500 11.5px "Ubuntu",sans-serif;color:var(--cyan);line-height:14px}
.body-copy{font-size:8px;line-height:11px}
.bullets{list-style:none;font-size:8px;line-height:11px}
.bullets li{position:relative;padding-left:15px}
.bullets li::before{content:"";position:absolute;left:0;top:3px;width:5px;height:5px;background:var(--cyan)}
.brand--inside{left:36px;top:372px;font-size:17px}
.contact{left:36px;top:398px;font-size:8px;line-height:11px}
.slogan{left:394px;top:148px;font:500 11.5px "Ubuntu",sans-serif;color:var(--cyan);line-height:14px}
.fold-note{left:394px;top:241px;font-size:4.5px;font-weight:700;color:var(--navy)}
.fold-line{left:394px;top:252px;width:273px;border-top:1px dashed var(--cyan)}
.reply-title{left:394px;top:257px;font:500 15px "Ubuntu",sans-serif;color:var(--cyan)}
.reply-lead{left:394px;top:280px;font-size:8px}
.reply-yes{left:394px;top:296px;font:700 14px "Ubuntu",sans-serif;color:var(--cyan)}
.option{left:394px;font-size:8px;display:flex;align-items:center;gap:3px}
.option .box{width:8px;height:8px;border:1px solid var(--cyan)}
.field{left:394px;width:273px;font-size:8px;border-bottom:1px solid var(--cyan);padding-bottom:1px}
</style>
</head>
<body>

<section class="sheet sheet--cover">
  <div class="abs reply-mark">
    <span class="letter">A</span>
    <span class="note">Nicht frankieren<br>Ne pas affranchir<br>Non affrancare</span>
    <span class="kind">Geschäftsantwortsendung &nbsp;Invio commerciale risposta<br>Envoi commercial-réponse</span>
  </div>

  <div class="abs brand brand--cover"><span class="brand__square"></span>VELUNA</div>

  <address class="abs recipient" style="font-style:normal">VELUNA IMMOBILIEN AG<br>Lindenweg 12<br>8004 Zürich</address>

  <div class="abs hero-photo" role="img" aria-label="Foto: modernes weisses Einfamilienhaus mit beleuchtetem Eingang, Holzsteg und Kiesgarten"></div>
  <div class="abs hero-edge"></div>
  <div class="abs hero-band">Immobilien sind unsere Passion</div>
  <div class="abs hero-accent"></div>

  <div class="abs cover-url">www. veluna-immo.ch</div>
</section>

<section class="sheet sheet--inside">
  <div class="abs side-bar side-bar--left"></div>
  <div class="abs side-bar side-bar--right"></div>
  <div class="abs tape tape--top">KLEBESTREIFEN</div>
  <div class="abs tape tape--bottom">KLEBESTREIFEN</div>
  <div class="abs perforation"></div>
  <svg class="abs scissors" viewBox="0 0 14 18" aria-hidden="true">
    <g fill="none" stroke="var(--cyan)" stroke-width="1.2">
      <line x1="3" y1="1" x2="9" y2="12"/><line x1="11" y1="1" x2="5" y2="12"/>
      <circle cx="4" cy="14.5" r="2.3"/><circle cx="10" cy="14.5" r="2.3"/>
    </g>
  </svg>

  <!-- left page -->
  <h2 class="abs page-title" style="left:36px;top:36px">Unsere Dienstleistungen</h2>
  <h3 class="abs sub-title" style="left:36px;top:74px">Verkauf mit Passion und Sachverstand</h3>
  <p class="abs body-copy" style="left:36px;top:87px">Der Verkauf einer Immobilie ist ein vielschichtiger Prozess. Lieb gewonnene<br>Liegenschaften, die über viele Jahre ein Zuhause waren, haben für die<br>Verkäufer nicht nur einen Geldwert, sondern auch einen emotionalen Wert.<br>Wir begleiten unsere Kunden mit Passion und Sachverstand durch jede Phase<br>des Verkaufsprozesses.</p>
  <ul class="abs bullets" style="left:36px;top:142px">
    <li>Erstes Gespräch und Besichtigung der Immobilie</li>
    <li>Ermitteln des bestmöglichen Verkaufspreises</li>
    <li>Erstellen von Verkaufsunterlagen und Vermarktung des Objekts</li>
    <li>Qualifizierern der Kaufinteressenten</li>
    <li>Finanzierungsberatung für Kaufinteressenten</li>
    <li>Preisverhandlungen und ausarbeiten des Kaufvertrags</li>
    <li>Begleitung bei der Beurkundung und Eigentumsübertragung</li>
  </ul>
  <h3 class="abs sub-title" style="left:36px;top:244px">Schätzung des Immobilienwerts</h3>
  <p class="abs body-copy" style="left:36px;top:257px">Damit unsere Kunden den bestmöglichen Preisfür ihr Haus, ihre Eigentums-<br>wohnung oder ihr Grundstück erzielen, ermitteln wir den genauen Wert.<br>Unsere Schätzung ergibt eine übersichtliche Aufstellung zum Gebäude,<br>der Lage, dem wirtschaftlichen Wert und Angaben zum Verkehrswert der<br>Immobilie. Wir wenden je nach Objekt die folgenden Bewertungsmethoden an:</p>
  <ul class="abs bullets" style="left:36px;top:312px">
    <li>Sachwert-, Ertragswert-oder Mischwertmethode</li>
    <li>Hedonische Bewertungen, Residualwertverfahren<br>oder DCF (Discounted-Cash-Flow-Verfahren)</li>
  </ul>
  <div class="abs brand brand--inside"><span class="brand__square"></span>VELUNA</div>
  <address class="abs contact" style="font-style:normal">VELUNA IMMOBILIEN AG<br>Lindenweg 12<br>8004 Zürich<br>Tel. 044 600 12 30<br>Fax 044 600 12 31<br>info@veluna-immo.ch<br>www. veluna-immo.ch</address>

  <!-- right page -->
  <h2 class="abs page-title" style="left:394px;top:36px">Unsere Werte und Visionen</h2>
  <p class="abs body-copy" style="left:394px;top:87px">Jede Immobilie ist so einzigartig, wie die Menschen, denen sie gehört.<br>Für uns zählt der Mensch, die Liegenschaft und die gemeinsame Geschichte.<br>In über 20 Jahren haben wir das Immobiliengeschäft und all seine Facetten<br>verinnerlicht. Das macht uns zu einem kompetenten und engagierten<br>Partner für alle Fragen rund um Immobilien.</p>
  <p class="abs slogan">Immobilien sind unsere Passion<br>und die Zufriedenheit der Kunden<br>ist unser Ziel.</p>

  <div class="abs fold-note">Bitte 1x falten und an den Klebestreifen zusammenkleben</div>
  <div class="abs fold-line"></div>
  <h3 class="abs reply-title">Rückantwort</h3>
  <p class="abs reply-lead">Bitte kreuzen Sie Ihre Wünsche an:</p>
  <p class="abs reply-yes">Ja,</p>
  <label class="abs option" style="top:316px"><span class="box"></span>... wir denken über einen Verkauf unserer Immobilie nach</label>
  <label class="abs option" style="top:334px"><span class="box"></span>... wir sind am Kauf einer Wohnung/Haus interessiert</label>
  <label class="abs option" style="top:352px"><span class="box"></span>... wir wünschen ein unverbindliches persönliches Gespräch</label>
  <div class="abs field" style="top:373px">Name/Vorname</div>
  <div class="abs field" style="top:395px">Strasse Nr.</div>
  <div class="abs field" style="top:417px">PLZ /Ort</div>
  <div class="abs field" style="top:439px">Telefon</div>
  <div class="abs field" style="top:461px">E-Mail</div>
</section>

</body>
</html>
```